SEO AND WEB DESIGN COMPANY BUSINESS CARD DESIGN

I need an eye catching , simple business card design that will match my logo . I need 2 versions of it ( white background and black background) - SOME PEOPLE DID NOT GET IT AND SENDING US FRONT WHITE BACK WHITE VERSIONS WHICH IS NOT CORRECT.

ONE VERSION SHOULD BE BACK AND FRONT ALL BLACK , SECOND VERSION SHOULD BE BACK AND FRONT ALL WHITE

logo psd files are attached for both versions. The business card is going to have : First Name- Last name - position - phone numbers

```html
<!DOCTYPE html>
<html lang="en">
<head>
<meta charset="utf-8">
<title>Brightpin – Business Card Set</title>
<link href="https://fonts.googleapis.com/css2?family=Montserrat:wght@500;600;700&display=swap" rel="stylesheet">
<style>
  :root {
    --blue: #2f8bff;
    --blue-deep: #1878ec;
    --blue-light: #3d98ff;
    --ink: #050505;
    --paper: #f7f9fc;
    --white: #ffffff;
    --stage: #e0e0e0;
  }
  * { margin: 0; padding: 0; box-sizing: border-box; }
  html, body { width: 1200px; height: 1200px; overflow: hidden; }
  body {
    position: relative;
    background: var(--stage);
    font-family: "Montserrat", sans-serif;
  }
  .panel { position: absolute; top: 0; height: 687px; }
  .panel--light { left: 0; width: 596px; background: var(--white); }
  .panel--dark { left: 604px; width: 596px; background: var(--ink); }
  .divider-vertical { position: absolute; left: 596px; top: 0; width: 8px; height: 694px; background: var(--blue); }
  .divider-horizontal { position: absolute; left: 0; top: 687px; width: 1200px; height: 7px; background: var(--blue); }

  .card { position: absolute; width: 504px; height: 288px; overflow: hidden; }
  .card--black { background: var(--ink); }
  .card--white { background: var(--paper); }
  .card--front-a { left: 46px; top: 57px; }
  .card--back-a  { left: 46px; top: 370px; }
  .card--front-b { left: 654px; top: 55px; }
  .card--back-b  { left: 654px; top: 370px; }

  .edge-tab {
    position: absolute; top: 110px; width: 18px; height: 67px;
    background: linear-gradient(180deg, var(--blue-light), var(--blue-deep));
  }
  .edge-tab--left { left: 0; border-radius: 0 18px 18px 0; }
  .edge-tab--right { right: 0; border-radius: 18px 0 0 18px; }

  .brand {
    position: absolute; display: flex; align-items: center; gap: 10px;
    color: var(--blue); font-weight: 700; white-space: nowrap;
  }
  .brand__dot { border-radius: 50%; background: var(--blue); flex: none; }
  .brand--large { left: 0; right: 0; top: 88px; justify-content: center; font-size: 46px; letter-spacing: 1px; }
  .brand--large .brand__dot { width: 30px; height: 30px; }
  .brand--small { right: 24px; top: 236px; font-size: 18px; gap: 6px; }
  .brand--small .brand__dot { width: 12px; height: 12px; }

  .website {
    position: absolute; left: 0; right: 0; top: 197px; text-align: center;
    font-size: 13px; font-weight: 700; letter-spacing: 4.4px;
  }
  .card--black .website { color: var(--white); }
  .card--white .website { color: var(--ink); }

  .name-band {
    position: absolute; left: 0; top: 29px; width: 260px; height: 60px;
    border-radius: 0 30px 30px 0;
    background: linear-gradient(90deg, var(--blue-deep), var(--blue-light));
  }
  .name { position: absolute; left: 49px; color: var(--ink); letter-spacing: 6px; line-height: 1; }
  .name--first { top: 38px; font-size: 21px; font-weight: 500; }
  .name--last { top: 63px; font-size: 21px; font-weight: 700; }
  .role {
    position: absolute; left: 49px; top: 101px;
    color: var(--blue); font-size: 16px; font-weight: 700; letter-spacing: 2.6px;
  }
  .contact { position: absolute; left: 49px; list-style: none; }
  .contact li {
    display: flex; align-items: center; gap: 14px; height: 30px;
    color: var(--blue); font-size: 16px; font-weight: 700; letter-spacing: 2.4px;
  }
  .contact li::before {
    content: ""; width: 7px; height: 7px; border-radius: 50%; background: var(--blue); flex: none;
  }
  .contact { top: 161px; }
</style>
</head>
<body>
  <section class="panel panel--light"></section>
  <section class="panel panel--dark"></section>
  <div class="divider-vertical"></div>
  <div class="divider-horizontal"></div>

  <!-- Black version -->
  <article class="card card--black card--front-a">
    <span class="edge-tab edge-tab--left"></span>
    <span class="edge-tab edge-tab--right"></span>
    <div class="brand brand--large"><span class="brand__dot"></span>BRIGHTPIN</div>
    <p class="website">BRIGHTPIN.CA</p>
  </article>

  <article class="card card--black card--back-a">
    <div class="name-band"></div>
    <p class="name name--first">MARCO</p>
    <p class="name name--last">SANTOS</p>
    <p class="role">GRAPHIC ARTIST</p>
    <ul class="contact">
      <li>+1 555 0148 221</li>
      <li>hello@brightpin.ca</li>
    </ul>
    <div class="brand brand--small"><span class="brand__dot"></span>BRIGHTPIN</div>
  </article>

  <!-- White version -->
  <article class="card card--white card--front-b">
    <span class="edge-tab edge-tab--left"></span>
    <span class="edge-tab edge-tab--right"></span>
    <div class="brand brand--large"><span class="brand__dot"></span>BRIGHTPIN</div>
    <p class="website">BRIGHTPIN.CA</p>
  </article>

  <article class="card card--white card--back-b">
    <div class="name-band"></div>
    <p class="name name--first">MARCO</p>
    <p class="name name--last">SANTOS</p>
    <p class="role">GRAPHIC ARTIST</p>
    <ul class="contact">
      <li>+1 555 0148 221</li>
      <li>hello@brightpin.ca</li>
    </ul>
    <div class="brand brand--small"><span class="brand__dot"></span>BRIGHTPIN</div>
  </article>
</body>
</html>
```